Criação de Power Point Slide Mestre para Advocacia e Direito
" Como pode observar, somos um escritório de advocacia voltado para empresas. Assim, as apresentaçoes ficam sempre voltadas para clientes efetivos ou em potencial. "

```html
<!DOCTYPE html>
<html lang="pt-BR">
<head>
<meta charset="UTF-8">
<title>Slide mestre – Moura &amp; Vidal</title>
<link rel="stylesheet" href="https://fonts.googleapis.com/css2?family=Open+Sans:wght@400;700&display=swap">
<style>
  :root {
    --page: #ffffff;
    --maroon-dark: #3f0710;
    --maroon: #7a1020;
    --maroon-light: #8e1a2c;
    --gold: #a48b5c;
    --gold-dark: #7e6840;
    --body: #f8f8f8;
    --ink: #111111;
    --white: #ffffff;
  }
  * { box-sizing: border-box; margin: 0; padding: 0; }
  html, body {
    width: 1200px; height: 1200px; overflow: hidden;
    background: var(--page);
    font-family: "Open Sans", sans-serif;
  }
  .slide {
    position: absolute; left: 40px; top: 180px;
    width: 1120px; height: 840px;
    background: var(--body);
    overflow: hidden;
  }
  .slide-shapes { position: absolute; inset: 0; }
  .brand {
    position: absolute; left: 40px; top: 52px;
    display: flex; align-items: center; gap: 16px;
    color: var(--white); font-size: 38px; font-weight: 400;
  }
  .brand-dot {
    width: 26px; height: 26px; border-radius: 50%;
    background: var(--gold);
  }
  .slide-title {
    position: absolute; right: 30px; top: 22px;
    width: 560px; text-align: center;
    color: var(--white); font-weight: 700;
  }
  .slide-title h1 { font-size: 44px; line-height: 56px; }
  .slide-title h2 { font-size: 40px; line-height: 50px; }
  .topics {
    position: absolute; left: 60px; top: 240px;
    list-style: none; color: var(--ink);
    font-size: 27px; line-height: 35px;
  }
  .topic-name { font-weight: 700; position: relative; padding-left: 24px; }
  .topic-name::before {
    content: ""; position: absolute; left: 2px; top: 14px;
    width: 10px; height: 10px; border-radius: 50%;
    background: var(--gold);
  }
  .topic-text { padding-left: 50px; }
  .topic-text.wide { padding-left: 42px; }
  .site {
    position: absolute; left: 0; right: 0; bottom: 12px;
    text-align: center; color: var(--white);
    font-size: 16px; font-weight: 700;
  }
</style>
</head>
<body>
  <section class="slide">
    <svg class="slide-shapes" viewBox="0 0 1120 840" width="1120" height="840" aria-hidden="true">
      <defs>
        <linearGradient id="header-grad" x1="0" y1="0" x2="1" y2="0">
          <stop offset="0" stop-color="var(--maroon)"/>
          <stop offset="1" stop-color="var(--maroon-dark)"/>
        </linearGradient>
        <linearGradient id="gold-grad" x1="0" y1="0" x2="1" y2="1">
          <stop offset="0" stop-color="var(--gold-dark)"/>
          <stop offset="1" stop-color="var(--gold)"/>
        </linearGradient>
      </defs>
      <path d="M1120 160 C1090 330 1070 600 1000 795 L1120 795 Z" fill="url(#gold-grad)"/>
      <rect x="0" y="0" width="1120" height="160" fill="url(#header-grad)"/>
      <path d="M0 0 L400 0 C420 60 410 120 380 160 L0 160 Z" fill="var(--maroon-light)"/>
      <rect x="0" y="795" width="1120" height="45" fill="var(--maroon)"/>
    </svg>

    <div class="brand"><span class="brand-dot"></span><span>Moura &amp; Vidal</span></div>

    <header class="slide-title">
      <h1>Título da apresentação</h1>
      <h2>1. TEXTO</h2>
    </header>

    <ul class="topics">
      <li class="topic-name">Tópico 1</li>
      <li class="topic-text">texto texto texto texto</li>
      <li class="topic-text">texto texto texto texto</li>
      <li class="topic-name">Tópico 2</li>
      <li class="topic-text">texto texto texto texto texto texto texto texto</li>
      <li class="topic-name">Tópico 3</li>
      <li class="topic-text">texto texto texto texto</li>
      <li class="topic-name">Tópico 4</li>
      <li class="topic-text wide">texto texto texto texto texto texto texto texto</li>
      <li class="topic-text wide">texto texto texto texto</li>
      <li class="topic-text wide">texto texto texto textotexto texto texto textotexto</li>
      <li class="topic-text wide">texto texto texto</li>
      <li class="topic-text wide">texto texto texto texto</li>
    </ul>

    <footer class="site">www.mouraevidal.com.br</footer>
  </section>
</body>
</html>
```